Homepage and Interior Page Design for BrontaLux

We will provide all logos, graphics and images as well as a wireframe of the desired homepage layout. Deliverables should be two well formated Photoshop files will well named layers, one for the homepage and one for an interior page. The "Puzzle Animation" will be developed separately. This will be a puzzle that breaks apart and reassembles to rotate the images. Here is the old site: https://www.brontalux.example/

Target Market(s)

Small to mid sized manufacturers.

Number of Pages Required

2 page

Font styles to use
Sans Serif

Colors

Designer to choose colors to be used in the design.

Requirements
Must have
• 2 layered photoshop files ready for slicing to HTML will well labeled layers
Nice to have
• If you are interested in creating the animation as a separate project, let me know.

```html
<!DOCTYPE html>
<html lang="en">
<head>
<meta charset="utf-8">
<title>BrontaLux — Packaging and Assembly Experts</title>
<link href="https://fonts.googleapis.com/css2?family=Nunito+Sans:wght@400;600&family=Poppins:wght@400;500;600&family=Roboto+Condensed:wght@400&display=swap" rel="stylesheet">
<style>
:root{
  --ink:#222;
  --muted:#555;
  --brand:#b8215a;
  --indigo:#3d3486;
  --band:#f0f1f6;
  --rose:#cd2f64;
  --charcoal:#2e2b29;
  --plum:#7c3e8c;
  --wood-light:#d8c59c;
  --wood-dark:#a88c5c;
  --line:#e6e6ea;
  --red:#e0202a;
}
*{margin:0;padding:0;box-sizing:border-box}
html,body{width:814px;height:1200px;overflow:hidden;background:#fff}
body{position:relative;font-family:"Poppins",sans-serif;color:var(--ink)}
.abs{position:absolute}

.header-phone{left:62px;top:28px;display:flex;align-items:center;gap:7px;font-size:10px;letter-spacing:.5px}
.logo{font-family:"Poppins",sans-serif;font-weight:600;color:var(--brand);letter-spacing:-.5px;white-space:nowrap;transform:translateX(-50%)}
.header-logo{left:436px;top:13px;font-size:27px}
.header-video{left:682px;top:29px;display:flex;align-items:center;gap:6px;font-size:10px}
.video-square{width:12px;height:12px;background:var(--red);border-radius:2px}

.main-nav{left:0;top:73px;width:814px;height:33px;background:var(--band)}
.main-nav a{position:absolute;top:10px;font-family:"Roboto Condensed",sans-serif;font-size:11px;color:#222;text-decoration:none;white-space:nowrap}

.hero{left:0;top:112px;width:337px;height:442px;background:var(--indigo);color:#fff;padding:108px 0 0 70px}
.hero h1{font-family:"Nunito Sans",sans-serif;font-weight:600;font-size:26px;line-height:34px;margin-bottom:20px}
.hero p{font-family:"Nunito Sans",sans-serif;font-size:11.5px;line-height:15px;width:240px;margin-bottom:15px}

.tile{width:126px;height:107px}
.tile.wood{background:linear-gradient(135deg,var(--wood-light),var(--wood-dark))}
.tile.label{display:flex;align-items:center;justify-content:center;text-align:center;color:#fff;font-family:"Nunito Sans",sans-serif;font-size:11.5px;line-height:14.5px;padding:0 10px}
.tile.rose{background:var(--rose)}
.tile.charcoal{background:var(--charcoal)}
.tile.plum{background:var(--plum)}

.service{width:160px}
.service-photo{width:158px;height:150px}
.service h3{font-size:10.5px;font-weight:500;line-height:13px;margin:32px 4px 6px}
.service p{font-size:9.5px;line-height:13px;color:var(--muted);margin:0 4px}
.read-more{position:absolute;font-size:8.5px;font-weight:600;color:#111;text-decoration:none}

.divider{left:0;top:942px;width:814px;height:1px;background:var(--line)}
.footer-logo{left:403px;top:972px;font-size:22px}
.contact{font-size:8.5px;line-height:18px;letter-spacing:.4px;color:#333}
.contact b{font-weight:600}
.contact-left{right:408px;top:1019px;text-align:right}
.contact-right{left:418px;top:1019px}
.footer-nav a{position:absolute;top:1091px;font-size:8.5px;letter-spacing:.4px;color:#333;text-decoration:none;white-space:nowrap}
.copyright-band{left:0;top:1149px;width:814px;height:51px;background:var(--band);font-size:8.5px;letter-spacing:.4px;text-align:center;line-height:51px;color:#333}
</style>
</head>
<body>

<div class="abs header-phone">
  <svg width="18" height="18" viewBox="0 0 18 18" aria-hidden="true">
    <circle cx="9" cy="9" r="8" fill="none" stroke="#c4285a" stroke-width="1.3"/>
    <path d="M6.3 5c.5-.3 1 .1 1.2.6l.5 1.2c.1.4 0 .7-.3.9l-.5.4c.4 1 1.3 2 2.4 2.5l.4-.5c.3-.3.6-.4.9-.3l1.2.5c.5.2.8.7.6 1.2-.3.8-1.1 1.3-2 1.1C8.3 12.1 5.8 9.6 5.3 7c-.2-.9.3-1.6 1-2z" fill="#c4285a"/>
  </svg>
  <span>555-201-7788</span>
</div>
<div class="abs logo header-logo">BrontaLux</div>
<div class="abs header-video"><span class="video-square"></span><span>VidStream</span></div>

<nav class="abs main-nav">
  <a style="left:83px">Home</a>
  <a style="left:134px">Contract Packaging</a>
  <a style="left:234px">Product Assembly</a>
  <a style="left:330px">Custom Pallets &amp; Crates</a>
  <a style="left:450px">Inventory Management &amp; Fulfillment</a>
  <a style="left:622px">About Us</a>
  <a style="left:684px">Contact Us</a>
</nav>

<section class="abs hero">
  <h1>Packaging and<br>Assembly Experts</h1>
  <p>BrontaLux is your one-stop source, from manufacturing to assembly to retail-ready packaging. We case-pack, print all standard bar code label formats, palletize and drop ship anywhere in the world.</p>
  <p>We can do as much or as little as you need… your call. 555-201-7788 or mail@brontalux.example.</p>
</section>

<div class="abs tile wood" style="left:374px;top:112px" role="img" aria-label="Stacked wooden pallets"></div>
<div class="abs tile wood" style="left:508px;top:112px" role="img" aria-label="Wooden pallet boards"></div>
<div class="abs tile label rose" style="left:640px;top:112px">Export Compliant Pallets and Crates, Retail Packaging Solutions</div>
<div class="abs tile label charcoal" style="left:402px;top:224px">Over 30 years<br>of excellence</div>
<div class="abs tile wood" style="left:534px;top:224px" role="img" aria-label="Stacked wooden pallets"></div>
<div class="abs tile wood" style="left:666px;top:224px" role="img" aria-label="Stacked wooden pallets"></div>
<div class="abs tile wood" style="left:441px;top:336px" role="img" aria-label="Wooden pallet stack"></div>
<div class="abs tile wood" style="left:572px;top:336px" role="img" aria-label="Wooden pallet stack"></div>
<div class="abs tile wood" style="left:356px;top:448px" role="img" aria-label="Wooden pallet stack"></div>
<div class="abs tile wood" style="left:489px;top:448px" role="img" aria-label="Wooden pallet stack"></div>
<div class="abs tile label plum" style="left:621px;top:448px">Product Assembly, Welding, cost-Free Tooling Programs</div>

<article class="abs service" style="left:62px;top:612px">
  <div class="service-photo" style="background:linear-gradient(135deg,#8a7a66,#c2ab85)" role="img" aria-label="Warehouse racks with flattened cardboard boxes"></div>
  <h3>Contract Packaging</h3>
  <p>We cover the spectrum of visible retail packaging, from blisters to clamshells to stretchpak, pouches, and bags.</p>
</article>
<a class="read-more" style="left:67px;top:880px">Read more</a>

<article class="abs service" style="left:242px;top:612px">
  <div class="service-photo" style="background:linear-gradient(135deg,#e6e8ef,#7c84a8)" role="img" aria-label="Close-up of assembly machinery"></div>
  <h3>Product Assembly</h3>
  <p>What sets us apart from other co-packers is our ability to assemble, repair and even manufacture your products.</p>
</article>
<a class="read-more" style="left:245px;top:879px">Read more</a>

<article class="abs service" style="left:421px;top:612px">
  <div class="service-photo" style="background:linear-gradient(135deg,#7a4f2c,#c08a55)" role="img" aria-label="Stacked wooden pallets"></div>
  <h3>Custom Pallets &amp; Crates</h3>
  <p>Our capabilities include certified export compliant pallets and crates. Custom sizes are what we do best.</p>
</article>
<a class="read-more" style="left:426px;top:883px">Read more</a>

<article class="abs service" style="left:593px;top:612px">
  <div class="service-photo" style="background:linear-gradient(135deg,#d9d6d2,#9bb0c8)" role="img" aria-label="Worker checking inventory in a warehouse"></div>
  <h3 style="margin-top:12px">Inventory Management<br>&amp; Fulfillment</h3>
  <p>You send us your products and they'll come back to you packaged and ready to sell. No worries, nothing to micro-manage.</p>
</article>
<a class="read-more" style="left:598px;top:883px">Read more</a>

<div class="abs divider"></div>

<footer>
  <div class="abs logo footer-logo">BrontaLux</div>
  <div class="abs contact contact-left"><b>Address:</b> 4270 Millbrook<br>Valley Rd Carrow Falls,<br>Ohio 40012</div>
  <div class="abs contact contact-right"><b>Phone:</b> 555-201-7788<br><b>Fax:</b> 555-201-7790<br><b>Email:</b> office@brontalux.example</div>
  <nav class="footer-nav">
    <a style="left:86px">Home</a>
    <a style="left:126px">Contract Packaging</a>
    <a style="left:227px">Product Assembly</a>
    <a style="left:318px">Custom Pallets &amp; Crates</a>
    <a style="left:444px">Inventory Management &amp; Fulfillment</a>
    <a style="left:618px">About Us</a>
    <a style="left:676px">Contact Us</a>
  </nav>
  <div class="abs copyright-band">Copyright © 2019 BrontaLux, Inc. All Right Reserved</div>
</footer>

</body>
</html>
```